Web Design for Small Healthcare Startup

Hello,

We are seeking a Website Design for a healthcare company focusing on mobile vaccinations, employee health and wellness services onsite at businesses, and consulting services relating to Healthcare Entities in WA state. Our company’s mission is to “To aid in a healthier workplace”. Brightpath Rovers will provide on-site wellness services to employers that simplify and streamline employee preventative health as well as onsite consulting services to help with compliance of Healthcare Entities.

We are seeking a Website Design for Brightpath Rovers, PLLC. Our company’s mission is to provide mobile health and wellness services to employers onsite at their businesses. These services include mobile vaccinations clinics for employees as well as wellness and health screenings. The company will also offer healtcare compliance consulting services for Healthcare Entities. The company was founded to bring these important healthcare services to businesses and keep employees healthy. Healthy employees are the cornerstone to a great business and we want to help orginazations achieve their goals of having a healthy productive workforce.

We are looking for a moderin website design that will need to be coded. We have attached our current logo design for reference as well as a brief questionare regarding our business for your information (not necessary to include all information). We would like something SEO friendly and easy to navigate.

Thank you!

Brightpath Rovers, PLLC

Target Market(s)

Small Businesses

Industry/Entity Type

Healthcare

Coding

Coded - Design and coding required

Number of Pages Required

1 page

Requirements
Nice to have
• SEO Friendly, Incorporate Logo

```html
<!DOCTYPE html>
<html lang="en">
<head>
<meta charset="utf-8">
<title>Brightpath Rovers, PLLC – On-site Mobile Vaccine Clinics</title>
<link rel="stylesheet" href="https://fonts.googleapis.com/css2?family=Inter:wght@400;500;600&family=Libre+Baskerville&display=swap">
<style>
:root{
  --primary:#0f55a8;
  --sky:#6aa9ec;
  --plum:#a4449c;
  --ink:#1d1d1f;
  --muted:#4d5560;
  --tint:#d4e5f8;
  --line:#c9ccd2;
  --white:#ffffff;
}
*{box-sizing:border-box;margin:0;padding:0}
html,body{width:1200px;height:4355px;overflow:hidden}
body{font-family:"Inter",sans-serif;color:var(--ink);background:var(--white);position:relative}
.serif{font-family:"Libre Baskerville",serif;font-weight:400}
.abs{position:absolute}
a{color:inherit}

.topbar{left:0;top:0;width:1200px;height:47px;background:var(--tint);font-size:14px;display:flex;justify-content:flex-end;align-items:center;gap:34px;padding-right:85px}
.topbar span{display:flex;align-items:center;gap:10px}

.nav{left:0;top:47px;width:1200px;height:114px;display:flex;align-items:center;padding:0 86px}
.brand{display:flex;align-items:center;gap:10px;font-weight:600;font-size:19px;color:var(--primary)}
.brand i{width:14px;height:14px;border-radius:50%;background:var(--plum);display:block}
.menu{margin-left:auto;display:flex;gap:32px;font-size:14px;font-weight:500;align-items:center}
.menu .on{color:var(--primary)}
.search{margin-left:48px;font-size:14px;font-weight:500;display:flex;align-items:center;gap:10px}
.btn-outline{margin-left:26px;border:2px solid var(--primary);color:var(--primary);border-radius:30px;padding:14px 22px;font-size:14px;font-weight:500}

.hero{left:0;top:161px;width:600px;height:660px;background:linear-gradient(135deg,#dbe8f7,#c8dcf3 60%,#d9e7f7)}
.hero-photo{left:600px;top:161px;width:600px;height:660px;background:linear-gradient(150deg,#eef1f4,#d8dde2 55%,#c9cfd6)}
.eyebrow{font-size:19px;font-weight:500;color:var(--primary)}
.hero h1{font-size:40px;line-height:53px;margin-top:18px;white-space:nowrap}
.ticks{list-style:none;margin-top:28px}
.ticks li{position:relative;padding-left:24px;font-size:15px;line-height:23px;color:var(--muted);margin-bottom:11px}
.ticks li::before{content:"";position:absolute;left:0;top:5px;width:13px;height:13px;border-radius:50%;background:var(--sky)}
.field{display:inline-flex;align-items:center;justify-content:space-between;width:194px;height:52px;border:2px solid var(--primary);border-radius:30px;padding:0 18px;font-size:14px;color:var(--primary);margin-right:12px}
.btn{display:inline-block;background:var(--primary);color:var(--white);border-radius:30px;padding:16px 30px;font-size:14px}

.notice{left:0;top:922px;width:1200px;text-align:center;font-size:15px;line-height:23px}

.docs{left:0;top:1072px;width:1200px;height:730px;background:linear-gradient(180deg,#d2e4f8,#ffffff 78%)}
.docs h2{position:absolute;left:84px;top:100px;font-size:36px}
.docs .intro{position:absolute;left:522px;top:100px;width:575px;font-size:15px;line-height:23px;color:var(--muted)}
.docs .intro p+p{margin-top:14px}
.step{position:absolute;top:331px;width:325px;height:368px;border-radius:6px;color:var(--white);padding:38px 31px}
.step b{display:block;font-size:14px;font-weight:600;margin-bottom:8px}
.step h3{font-size:22px;line-height:33px;position:relative;z-index:1}
.step .art{position:absolute;right:28px;bottom:20px;width:140px;height:145px;border-radius:8px;background:rgba(255,255,255,.18)}

.services{left:86px;top:1870px;width:1030px}
.services h2{font-size:37px;margin-top:14px}
.services .ticks{margin-top:30px}
.services .ticks li{font-size:15px;margin-bottom:16px}

.about{left:86px;top:2466px;width:1028px;height:514px;background:var(--primary);border-radius:18px;color:var(--white)}
.about .art{position:absolute;left:48px;top:40px;width:450px;height:474px;border-radius:10px 10px 0 0;background:linear-gradient(180deg,#dfe7ef,#b8c7d6)}
.about .copy{position:absolute;left:528px;top:60px;width:440px}
.about h2{font-size:35px;line-height:48px;margin-top:16px}
.about p{font-size:15px;line-height:23px;margin-top:28px}
.about p+p{margin-top:22px}

.schedule{left:0;top:3075px;width:1200px;text-align:center}
.schedule h2{font-size:37px}
.schedule .sub{font-size:15px;line-height:23px;color:var(--muted);margin-top:16px}
.nums{display:flex;justify-content:space-between;width:1000px;margin:34px auto 0}
.nums div{width:300px;font-size:19px;font-weight:500;line-height:26px}
.nums span{display:block;margin:0 auto 18px;width:58px;height:58px;border-radius:50%;background:var(--primary);color:var(--white);font-family:"Libre Baskerville",serif;font-size:22px;line-height:58px}

.pricing{left:0;top:3465px;width:1200px;height:524px;background:linear-gradient(90deg,#ffffff 35%,#e3edf9)}
.pricing .art{position:absolute;left:608px;top:0;width:490px;height:524px;background:linear-gradient(160deg,#cfe0f1,#9dbbd9 60%,#d8e6f4)}
.pricing .copy{position:absolute;left:86px;top:84px;width:500px}
.pricing h2{font-size:35px;line-height:46px;margin-top:14px;white-space:nowrap}
.pricing .lead{font-size:15px;line-height:23px;margin-top:28px;width:470px}
.pricing .st{font-size:15px;line-height:23px;color:var(--muted);margin-top:14px;width:470px}

.footer{left:0;top:4100px;width:1200px;text-align:center}
.footer .brand{justify-content:center;font-size:22px}
.footer .links{width:1028px;margin:46px auto 0;border-top:1px solid var(--line);border-bottom:1px solid var(--line);padding:14px 0;display:flex;justify-content:center;gap:32px;font-size:14px;font-weight:500}
.footer small{display:block;margin-top:22px;font-size:14px}
</style>
</head>
<body>

<div class="abs topbar">
  <span><svg width="16" height="12" viewBox="0 0 16 12" fill="none" stroke="#4d5560"><rect x=".5" y=".5" width="15" height="11"/><path d="M1 1l7 6 7-6"/></svg>Email: hello@brightpathrovers.example</span>
  <span><svg width="14" height="14" viewBox="0 0 24 24" fill="none" stroke="#4d5560" stroke-width="2"><path d="M22 16.9v3a2 2 0 0 1-2.2 2A19.8 19.8 0 0 1 2.1 4.2 2 2 0 0 1 4.1 2h3a2 2 0 0 1 2 1.7c.1 1 .4 1.9.7 2.8a2 2 0 0 1-.5 2.1L8 9.900a16 16 0 0 0 6 6l1.3-1.300a2 2 0 0 1 2.1-.4c.9.3 1.8.6 2.8.7a2 2 0 0 1 1.7 2z"/></svg>Phone: 555-014-2277</span>
</div>

<header class="abs nav">
  <div class="brand"><i></i>Brightpath Rovers</div>
  <nav class="menu"><span class="on">Home</span><span>About</span><span>Services ⌄</span><span>Pricing</span></nav>
  <div class="search">Search <svg width="16" height="16" viewBox="0 0 24 24" fill="none" stroke="#1d1d1f" stroke-width="2.5"><circle cx="10" cy="10" r="7"/><path d="M15 15l6 6"/></svg></div>
  <span class="btn-outline">Appointment</span>
</header>

<section class="abs hero">
  <div style="position:absolute;left:86px;top:62px;width:430px">
    <div class="eyebrow">Brightpath Rovers, PLLC</div>
    <h1 class="serif">Making the workplace<br>a healthier place.</h1>
    <ul class="ticks">
      <li>Brightpath Rovers specializes in providing seamless, hassle-free, on-site mobile vaccine clinics.</li>
      <li>No crowded waiting rooms, no long lines, no hassle!</li>
      <li>Specializing in workplace employee vaccine clinics.Great service to offer as part of your company's Employee Wellness Package.</li>
      <li>Offering Flu and Covid vaccinations Reserve your on-site mobile vaccine clinic today!</li>
    </ul>
    <div style="margin-top:26px"><span class="field">Choose Date <svg width="16" height="16" viewBox="0 0 16 16" fill="none" stroke="#0f55a8"><rect x="1.5" y="2.5" width="13" height="12"/><path d="M1.5 6h13M5 1v3M11 1v3"/></svg></span><span class="field">Choose Time <svg width="17" height="17" viewBox="0 0 16 16" fill="none" stroke="#0f55a8"><circle cx="8" cy="8" r="6.5"/><path d="M8 4v4l3 2"/></svg></span></div>
    <div style="margin-top:18px"><span class="btn">Book Now</span></div>
  </div>
</section>
<div class="abs hero-photo" role="img" aria-label="Photo of a caregiver's hands holding a heart beside a stethoscope, notebook and laptop"></div>

<p class="abs notice">STATE HEALTH OFFICE FLU SHOT RECOMMENDATIONS (yearly flu shot between Aug -Dec?) <a href="#" style="font-weight:500">Learn More</a><br>Or call directly for more information</p>

<section class="abs docs">
  <h2 class="serif">Dana's documents</h2>
  <div class="intro">
    <p>Avoid long lines ... Each employee can sign up for specific time or dept managers can release employees in phases to clinic. Also available: book for entire day so employees can get vaccinated as their workload permits.</p>
    <p>Employees will avoid congested waiting rooms at medical offices and long lines at local pharmacies</p>
  </div>
  <div class="step" style="left:86px;background:var(--primary)"><b>STEP 1</b><h3 class="serif">Submit Vaccine<br>Clinic Needs<br>Questionnaire.</h3><div class="art" role="img" aria-label="Illustration of a nurse with a clipboard, syringe and stethoscope"></div></div>
  <div class="step" style="left:438px;background:var(--sky)"><b>STEP 2</b><h3 class="serif">Brightpath Rovers,<br>PLLC will contact<br>you to schedule<br>on-site vaccine clinic.</h3><div class="art" role="img" aria-label="Illustration of two doctors standing together"></div></div>
  <div class="step" style="left:789px;background:var(--plum)"><b>STEP 3</b><h3 class="serif">Prepare your<br>employees for<br>vaccine clinic day.</h3><div class="art" role="img" aria-label="Illustration of a doctor with a speech bubble"></div></div>
</section>

<section class="abs services">
  <div class="eyebrow">Our Services</div>
  <h2 class="serif">Brightpath Rovers will come to you!</h2>
  <ul class="ticks">
    <li>No crowded waiting rooms, no long lines, no hassle!</li>
    <li>Hassle-free, streamlining the vaccination process ... provide this on-site service as part of your employee wellness package</li>
    <li>Serving employers who want to increase the health and Wellness of their workplace</li>
    <li>vaccines including seasonal flu, COVID, Pneumonia</li>
    <li>Ensure your employees and their families remain healthy this flu season. Host a flu shot clinic on site to help your employees<br>get vaccinated. Provide this service as part of your employee Wellness benefits package.</li>
    <li>Brightpath Rovers specializes in providing seamless, hassle-free vaccine clinics.</li>
    <li>Don't wait for your employees to get their vaccines at their next doctor's appointment or visit to the pharmacy. Provide this<br>desired employee benefit on site with no crowded waiting rooms, no long lines, no hassle!</li>
    <li>Create a healthier, happier workplace with this desired employee health benefit.</li>
    <li>Brightpath Rovers also offers consulting services for WA Healthcare Entities.</li>
  </ul>
</section>

<section class="abs about">
  <div class="art" role="img" aria-label="Photo of two masked medical professionals in white coats"></div>
  <div class="copy">
    <div style="font-size:19px;font-weight:500">About Brightpath Rovers, PLLC</div>
    <h2 class="serif">Pharmacist owned and<br>operated.</h2>
    <p>To provide on-site wellness services to employers that simplify and streamline employee preventative health.</p>
    <p>Brightpath Rovers, PLLC was started by local, Washington state licensed pharmacist with over 15 years experience vaccinating patients. She is a highly skilled immunizer and enjoys interacting with patients while providing this important preventative health services. Her vaccination experience spans from individual patient vaccinations to large clinics during community outbreaks.</p>
  </div>
</section>

<section class="abs schedule">
  <h2 class="serif">Schedule Today:</h2>
  <p class="sub">Hassle-free, streamlining the vaccination process ...<br>Submit this simple Vaccine Clinic Needs Questionnaire and Brightpath Rovers will do the rest.</p>
  <div class="nums">
    <div><span>01</span>Submit Vaccine Clinic Needs Questionnaire.</div>
    <div><span>02</span>Brightpath Rovers, PLLC will contact you to schedule on-site vaccine clinic.</div>
    <div><span>03</span>Prepare your employees for vaccine clinic day.</div>
  </div>
</section>

<section class="abs pricing">
  <div class="art" role="img" aria-label="Photo of two medical workers in protective gowns, masks and goggles"></div>
  <div class="copy">
    <div class="eyebrow">Our Pricing</div>
    <h2 class="serif">Hassle-free, streamlining<br>the vaccination process ...</h2>
    <p class="lead">Price quote is simple! No hidden travel/mileage calculations, no hidden hourly fees.</p>
    <p class="st" style="margin-top:20px">Step 1: Submit Vaccine Clinic Needs Questionnaire.</p>
    <p class="st">Step 2: Brightpath Rovers, PLLC will contact you to schedule on-site vaccine clinic.</p>
    <p class="st">Step 3: Prepare your employees for vaccine clinic day.</p>
  </div>
</section>

<footer class="abs footer">
  <div class="brand"><i></i>Brightpath Rovers</div>
  <nav class="links"><span>Home</span><span>About</span><span>Services</span><span>Pricing</span></nav>
  <small>Copyright 2022.All right reserved.</small>
</footer>

</body>
</html>
```